Contemporary Business card for Event Manager

Needed for my startup events company in Melbourne. Events I manage will be based within the fashion industry, sporting events, product launches etc. Not weddings or small dinner parties. Therfore I am after something professional and aimed at high end corporate market; but with the added emphasis on not being too conservative or boring. I am happy with a pop of colour e.g. yellow or copper foil.

Target Market(s)

fashion industry, design industry, high end sporting events e.g. Polo, Grand Prix, corporate clients,

Industry/Entity Type

Fashion

Contact Information for Business Card

side 1
Lena Varsby (can be upper or lower case, have a feature full stop between first and surname, or at the end of the nameetc) I am open to ideas. I would also be fine with my initials or name as a logo on the front (if this is the case my full name would need to go on the second side of the card.
2nd side:
Mobile: +61 491 570 156
email: lena.varsby@mailtrove.com.au

on one side of the card:
event management | brand activation | Advisory Services

Font styles to use
Serif
Sans Serif

Requirements
Must have
• side 2 must have
• mobile number
• email address
• event management | brand activation | Advisory Services
• ** my full name (Lena Varsby) must be on the card somewhere)
Nice to have
• 1st side
• I see the card stock being either a dark grey, light grey, natural white or black (all matt colours on unprocessed card). I see the writing being copper foil, or foil white or foil black.
• To give you a feel for me, think: contemporary, minimalist, I love line drawings, concrete, white with grey vein marble, copper, white, grey, black...yes I do like colour....yellow (but pops of colour) ;) I would like the card to look designer but 'on trend' as I deal with a lot of design and fashion clients....styles - think the sophistication and simplicity of Morvane or urban contemporary.
• some examples of what I like. Although please don't leet this limit you...I really am happy to have something a little more urban or design focused like a line drawing of an object, person too or a photo image too.
• https://www.moodfolia.com/pin/100000000000000001/
• https://www.moodfolia.com/pin/100000000000000002/
• https://www.moodfolia.com/pin/100000000000000003/
• https://www.moodfolia.com/pin/10000000000000004/
• https://www.moodfolia.com/pin/10000000000000005/
• https://www.moodfolia.com/pin/10000000000000006/
• https://www.moodfolia.com/pin/100000000000000007/
• https://www.moodfolia.com/pin/100000000000000008/
• https://www.moodfolia.com/pin/100000000000000009/
Should not have
• should not look commercial or have cartoonish looking logos. However happy with a simple line drawing or logo with initials etc.

```html
<!DOCTYPE html>
<html lang="en">
<head>
<meta charset="UTF-8">
<title>Lena Varsby – Business Card</title>
<link href="https://fonts.googleapis.com/css2?family=Lato:wght@300;400;700&family=Cinzel:wght@400&display=swap" rel="stylesheet">
<style>
  :root {
    --backdrop: #ece9e4;
    --copper-light: #cf7434;
    --copper-mid: #b35a25;
    --copper-dark: #86391a;
    --gold-yellow: #f2c31b;
    --card-yellow: #ecd222;
    --card-yellow-deep: #d8b90f;
    --emboss-dark: rgba(120, 96, 0, 0.55);
    --emboss-light: rgba(255, 250, 190, 0.85);
    --text-white: #fbf4ee;
    --icon-fill: #e9e3df;
    --icon-ink: #6a3a20;
  }
  * { margin: 0; padding: 0; box-sizing: border-box; }
  html, body {
    width: 1200px;
    height: 1023px;
    overflow: hidden;
    background: var(--backdrop);
  }
  .canvas {
    width: 1200px;
    height: 1023px;
    display: flex;
    flex-direction: column;
    align-items: center;
    justify-content: center;
    gap: 56px;
  }
  .card {
    width: 700px;
    height: 400px;
    border-radius: 26px;
    position: relative;
    box-shadow: 0 10px 28px rgba(60, 40, 20, 0.25);
    overflow: hidden;
  }
  .card-back {
    background: linear-gradient(135deg, var(--copper-light) 0%, var(--copper-mid) 50%, var(--copper-dark) 100%);
    font-family: "Lato", sans-serif;
    color: var(--text-white);
  }
  .contact-block {
    position: absolute;
    left: 58px;
    bottom: 54px;
  }
  .holder-name {
    font-weight: 700;
    font-size: 30px;
    color: var(--gold-yellow);
    letter-spacing: -0.2px;
    line-height: 1.1;
  }
  .holder-role {
    font-weight: 300;
    font-size: 19px;
    margin-top: 6px;
    opacity: 0.92;
  }
  .contact-list {
    list-style: none;
    margin-top: 18px;
  }
  .contact-item {
    display: flex;
    align-items: center;
    gap: 10px;
    font-weight: 300;
    font-size: 21px;
    line-height: 1.6;
  }
  .contact-icon {
    width: 24px;
    height: 24px;
    flex: none;
  }
  .services {
    margin-top: 22px;
    font-weight: 700;
    font-size: 21px;
    letter-spacing: 0.1px;
  }
  .card-front {
    background: linear-gradient(150deg, var(--card-yellow) 0%, var(--card-yellow-deep) 100%);
    display: flex;
    align-items: center;
    justify-content: center;
  }
  .front-name {
    font-family: "Cinzel", serif;
    font-weight: 400;
    font-size: 50px;
    letter-spacing: 2px;
    color: var(--card-yellow-deep);
    text-shadow: -1px -1px 1px var(--emboss-dark), 1px 1px 1px var(--emboss-light);
  }
</style>
</head>
<body>
  <main class="canvas">
    <section class="card card-back" aria-label="Card back with contact details">
      <div class="contact-block">
        <h1 class="holder-name">Lena Varsby</h1>
        <p class="holder-role">Owner</p>
        <ul class="contact-list">
          <li class="contact-item">
            <svg class="contact-icon" viewBox="0 0 24 24" aria-hidden="true">
              <circle cx="12" cy="12" r="12" fill="var(--icon-fill)"/>
              <path d="M8.3 6.5c.4-.4 1-.4 1.3 0l1.4 1.8c.3.4.3.9-.1 1.2l-.8.8c.5 1.3 1.5 2.4 2.8 3l.8-.8c.3-.4.9-.4 1.2-.1l1.8 1.4c.4.3.4.9 0 1.3l-1 1c-.6.6-1.5.7-2.3.4-2.8-1.1-4.9-3.3-6-6-.3-.8-.2-1.7.4-2.3z" fill="var(--icon-ink)"/>
            </svg>
            <span>+61 491 570 156</span>
          </li>
          <li class="contact-item">
            <svg class="contact-icon" viewBox="0 0 24 24" aria-hidden="true">
              <circle cx="12" cy="12" r="12" fill="var(--icon-fill)"/>
              <rect x="6" y="8" width="12" height="8.5" rx="1" fill="none" stroke="var(--icon-ink)" stroke-width="1.4"/>
              <path d="M6.4 8.6 12 13l5.6-4.4" fill="none" stroke="var(--icon-ink)" stroke-width="1.4"/>
            </svg>
            <span>lena.varsby@mailtrove.com.au</span>
          </li>
        </ul>
        <p class="services">Event management | Brand activation | Advisory Services</p>
      </div>
    </section>

    <section class="card card-front" aria-label="Card front with name">
      <h2 class="front-name">LENA VARSBY</h2>
    </section>
  </main>
</body>
</html>
```